Banner Ad Design Project

I need a banner design. The website is under construction at www.brightmarrow.example

Name: Bright Marrow
Tagline: Steady Sparks for crowded calendars

This is a leadership development and executive coaching site. The past site is live at www.quillstepnow.example. (so you can get a sense of the content)

The audience are (BUSY) executives, senior managers, leaders and top professionals, so the feel needs to be highly professional but also modern and fresh. I want to communicate energy but also solid and trust worthy and not too new agey. The audience are also people with strong social values who want to change things - so not too corporate (Ie suits!)

I would like the design to be floating on a white background, very clean and simple. I am attracted to reds or sunset (burn orange crimson colors.) But totally open to any color ideas.
I am giving an open brief for your ideas.
Here are the dimensions 960px wide, roughly 190px height.

Reason: The weekend might give more time to designers to get involved. Thanks Vina

Hi designers

You may not have seen the additions I gave to this brief.

The banner should not have leader out front photo's. Maybe less corporate than I initially thought. 
Not too corporate (no suits!) Please no chess pieces, jigsaw pieces, cartoon images, cliche leadership images. 
Am am trying for inspiration /inspiring whilst still being professional. Very simple and clean.
Please can the design be floating in a white background so that the web page is borderless - A bit like it is in http://palmoriskel.example/
Thank you

Target Market(s)

Senior managers, executives but people who also want to change the world!

Industry/Entity Type

Construction

Requirements
Should not have
• Should not have leader out front photo's.
Maybe less corporate than I initially thought.
Am am trying for inspiration /inspiring whilst still being professional.
Please no chess pieces, jigsaw pieces, cartoon images, cliche leadership images. Not too corporate (Ie suits!)

Thanks

```html
<!DOCTYPE html>
<html lang="en">
<head>
<meta charset="utf-8">
<title>Bright Marrow banner</title>
<link rel="stylesheet" href="https://fonts.googleapis.com/css2?family=Roboto:wght@300&family=Arimo:wght@400&display=swap">
<style>
  :root {
    --page: #ffffff;
    --frame: #cfcfcf;
    --brand-red: #d0111b;
    --ink: #1a1a1a;
    --rule: #9a9a9a;
    --stripe: #f1f1f1;
    --crowd-light: #f4f4f4;
    --crowd-mid: #d9d9d9;
    --crowd-red: #c8161d;
  }
  html, body {
    margin: 0;
    padding: 0;
    width: 1200px;
    height: 270px;
    overflow: hidden;
    background: var(--page);
  }
  .banner {
    position: relative;
    width: 1200px;
    height: 270px;
    background: var(--page);
  }
  .banner-frame {
    position: absolute;
    left: 10px;
    top: 22px;
    width: 1176px;
    height: 234px;
    border: 1px solid var(--frame);
    box-sizing: border-box;
    overflow: hidden;
  }
  .corner-stripes {
    position: absolute;
    right: 0;
    top: 0;
  }
  .crowd-illustration {
    position: absolute;
    left: 14px;
    top: 0;
    width: 400px;
    height: 232px;
    background:
      radial-gradient(ellipse 60px 70px at 65% 88%, var(--crowd-red) 0%, rgba(200,22,29,0.7) 45%, rgba(200,22,29,0) 100%),
      linear-gradient(160deg, var(--crowd-mid) 0%, var(--crowd-light) 55%, var(--page) 100%);
  }
  .brand-name {
    position: absolute;
    left: 480px;
    top: 52px;
    margin: 0;
    font-family: "Roboto", Helvetica, Arial, sans-serif;
    font-weight: 300;
    font-size: 104px;
    line-height: 1;
    letter-spacing: -1px;
    color: var(--brand-red);
    white-space: nowrap;
  }
  .tagline-row {
    position: absolute;
    left: 480px;
    top: 186px;
    display: flex;
    align-items: center;
    gap: 10px;
  }
  .tagline-rule {
    width: 202px;
    height: 1px;
    background: var(--rule);
  }
  .tagline {
    margin: 0;
    font-family: "Arimo", Arial, sans-serif;
    font-size: 21px;
    letter-spacing: 0.6px;
    color: var(--ink);
    white-space: nowrap;
  }
</style>
</head>
<body>
  <div class="banner">
    <div class="banner-frame">
      <svg class="corner-stripes" width="170" height="120" viewBox="0 0 170 120" aria-hidden="true">
        <polygon points="70,0 110,0 40,120 0,120" fill="var(--stripe)"/>
        <polygon points="130,0 170,0 100,120 60,120" fill="var(--stripe)"/>
      </svg>
      <div class="crowd-illustration" role="img" aria-label="Illustration of a crowd of pale grey figures arranged in a wedge, led by a single red figure at the front"></div>
      <h1 class="brand-name">Bright Marrow</h1>
      <div class="tagline-row">
        <span class="tagline-rule"></span>
        <p class="tagline">Steady Sparks for crowded calendars</p>
      </div>
    </div>
  </div>
</body>
</html>
```